Flyer Design / Authenticity Certificate - Art Work

Looking for a design of a "Authenticity Certificate" - flyer, that will include some basic company info like logo etc, and allow our in house artist to sign and authenticate before it is applied the reverse of one of the paintings we will sell. Linked with our online sales website - "Copper Hollow Canvases", where we recreate one off oil paintings from digital photographs. Our business logo should be incorporated in the design, along with a section for "Artisit Name" "Artisit Signature" "Ref Code"
Updates

Hi.. Sorry I should have added the size we need - please design accordingly to A6. Thanks.

Industry/Entity Type

It Company

Font styles to use
Serif
Script

Colors

Designer to choose colors to be used in the design.

Requirements
Must have
• Company logo
• Area for artist to print and sign
• Area for a reference
Nice to have
• must use the logo, maybe incorporate a "seal" icon, like what was used as a wax seal on older style documents

```html
<!DOCTYPE html>
<html lang="en">
<head>
<meta charset="utf-8">
<title>Certificate of Authenticity – Copper Hollow Canvases</title>
<link rel="stylesheet" href="https://fonts.googleapis.com/css2?family=Cinzel:wght@400;700&family=Great+Vibes&family=Source+Sans+3:wght@400;500&display=swap">
<style>
  :root {
    --ink-black: #0c0c0c;
    --panel-grey: #7f7f80;
    --mark-grey: #4b4b4c;
    --brand-light: #e9e9e9;
    --band-red: #e8262b;
    --band-red-light: #f2462a;
    --band-green: #9ac83c;
    --band-orange: #f39322;
    --paper: #f4f4f4;
    --paper-shade: #e4e5e7;
    --text-dark: #1e1e1e;
    --script-ink: #3b3b3b;
    --dot-red: #e03a3a;
    --gold-light: #f1c15a;
    --gold-mid: #d08d22;
    --gold-dark: #8a5410;
  }
  html, body {
    margin: 0;
    padding: 0;
    width: 1200px;
    height: 851px;
    overflow: hidden;
    background: var(--paper);
  }
  .certificate {
    position: relative;
    width: 1200px;
    height: 851px;
    overflow: hidden;
    background: linear-gradient(180deg, var(--paper) 0%, #fafafa 45%, var(--paper-shade) 100%);
    font-family: "Source Sans 3", "Helvetica Neue", Arial, sans-serif;
    color: var(--text-dark);
  }
  .backdrop {
    position: absolute;
    inset: 0;
  }
  .brand-name {
    position: absolute;
    left: 62px;
    top: 222px;
    width: 351px;
    margin: 0;
    text-align: center;
    font-family: "Source Sans 3", "Helvetica Neue", Arial, sans-serif;
    font-weight: 500;
    font-size: 25px;
    letter-spacing: 1.5px;
    text-transform: uppercase;
    color: var(--brand-light);
  }
  .title {
    position: absolute;
    left: 440px;
    width: 720px;
    margin: 0;
    text-align: center;
    font-family: "Cinzel", "Times New Roman", serif;
    color: #ffffff;
    font-weight: 400;
  }
  .title-main {
    top: 48px;
    font-size: 86px;
    line-height: 1;
    letter-spacing: 1px;
  }
  .title-sub {
    top: 160px;
    font-size: 44px;
    line-height: 1;
    letter-spacing: 1px;
  }
  .statement {
    position: absolute;
    left: 560px;
    top: 396px;
    width: 480px;
    margin: 0;
    text-align: center;
    font-size: 29px;
    line-height: 34px;
  }
  .artist-name {
    position: absolute;
    left: 440px;
    top: 470px;
    width: 740px;
    margin: 0;
    text-align: center;
    font-family: "Great Vibes", "Brush Script MT", cursive;
    font-size: 128px;
    line-height: 1.2;
    color: var(--script-ink);
    font-weight: 400;
  }
  .signature-line {
    position: absolute;
    left: 585px;
    top: 732px;
    width: 432px;
    border-top: 3px dotted var(--dot-red);
  }
  .signature-label {
    position: absolute;
    left: 585px;
    top: 742px;
    width: 432px;
    text-align: center;
    font-size: 19px;
    letter-spacing: 0.3px;
  }
  .reference-label,
  .reference-code {
    position: absolute;
    top: 807px;
    font-size: 20px;
    letter-spacing: 0.3px;
  }
  .reference-label {
    left: 470px;
  }
  .reference-code {
    right: 82px;
  }
</style>
</head>
<body>
<main class="certificate">
  <svg class="backdrop" width="1200" height="851" viewBox="0 0 1200 851" aria-hidden="true">
    <defs>
      <linearGradient id="header-sheen" x1="0" y1="0" x2="1" y2="0">
        <stop offset="0" stop-color="#1c1c1c"/>
        <stop offset="0.6" stop-color="#101010"/>
        <stop offset="1" stop-color="#050505"/>
      </linearGradient>
      <linearGradient id="red-band" x1="0" y1="0" x2="1" y2="0">
        <stop offset="0" stop-color="var(--band-red)"/>
        <stop offset="0.5" stop-color="var(--band-red-light)"/>
        <stop offset="1" stop-color="var(--band-red)"/>
      </linearGradient>
    </defs>
    <path class="header-field" d="M0 0 H1200 V216 L488 364 L0 308 Z" fill="url(#header-sheen)"/>
    <path class="band-green" d="M488 364 L1200 216 V242 L560 372 Z" fill="var(--band-green)"/>
    <path class="band-orange" d="M540 375 L1200 240 V262 L600 377 Z" fill="var(--band-orange)"/>
    <path class="band-red" d="M0 308 L595 375 L480 401 L0 348 Z" fill="url(#red-band)"/>
    <rect class="brand-panel" x="62" y="0" width="351" height="316" fill="var(--panel-grey)"/>
    <circle class="brand-dot" cx="238" cy="106" r="82" fill="var(--mark-grey)"/>
  </svg>

  <p class="brand-name">Copper Hollow Canvases</p>

  <h1 class="title title-main">Certificate</h1>
  <h2 class="title title-sub">Of Authenticity</h2>

  <svg class="seal" style="position:absolute;left:62px;top:428px" width="370" height="370" viewBox="0 0 370 370" role="img" aria-label="Gold wax seal of authenticity">
    <defs>
      <radialGradient id="seal-gold" cx="0.38" cy="0.35" r="0.7">
        <stop offset="0" stop-color="var(--gold-light)"/>
        <stop offset="0.55" stop-color="var(--gold-mid)"/>
        <stop offset="1" stop-color="var(--gold-dark)"/>
      </radialGradient>
    </defs>
    <circle cx="185" cy="185" r="178" fill="url(#seal-gold)"/>
  </svg>

  <p class="statement">This is to certify that<br>this Artwork is Authentic</p>

  <p class="artist-name">Artist Name</p>

  <div class="signature-line"></div>
  <div class="signature-label">ARTIST SIGNATURE</div>

  <div class="reference-label">REFERENCE CODE:</div>
  <div class="reference-code">ABC-1234-XXX</div>
</main>
</body>
</html>
```